Sports guard Postcard

We are opening a new dental office in Mead, WA and would like to market to the young families that are involved in sports programs.
What we are looking for on a post card are pictures of young athletes playing football, soccer, basketball and hockey and than talk a bit about the importance of sports guard when you are doing sports. Our marketing campaign is to do free sports guards to students who can show that they are signed up with a team. I will send you a copy of our logo so you can see what our colors are.

Here is our address, phone number and web site for the mailing side. Cedar Brook Dental 22856 W. Larkfield Ave. Suite B Mead, WA 99021 509-738-1946 CedarbrookDentist.example

I just realized a error that I made. These sports guard are to be mouth guard for teeth. Hope that was not confusing.

```html
<!DOCTYPE html>
<html lang="en">
<head>
<meta charset="utf-8">
<title>Cedar Brook Dental – Free Sports Guards Postcard</title>
<link rel="stylesheet" href="https://fonts.googleapis.com/css2?family=Source+Sans+3:wght@300;400;600&display=swap">
<style>
  :root {
    --backdrop: #1f1f1f;
    --paper: #ffffff;
    --plum: #7a1f4f;
    --plum-dark: #5f1239;
    --olive: #5f5b17;
    --olive-dark: #4a4710;
    --ink: #3a3a3a;
    --on-dark: #ffffff;
    --grass: #6f9a3a;
    --grass-light: #a9c46c;
    --portrait: #d9d9d9;
  }
  * { box-sizing: border-box; margin: 0; padding: 0; }
  html, body {
    width: 1200px; height: 1200px; overflow: hidden;
    background: var(--backdrop);
    font-family: "Source Sans 3", sans-serif;
    font-weight: 300;
  }
  .stage { position: relative; width: 1200px; height: 1200px; }
  .postcard {
    position: absolute; background: var(--paper); overflow: hidden;
  }
  .block { position: absolute; }
  .photo { position: absolute; }

  /* mailing side */
  .mailing-side { left: 419px; top: 25px; width: 727px; height: 559px; }
  .mailing-side .photo-player { left: 0; top: 0; width: 352px; height: 176px;
    background: linear-gradient(135deg, var(--grass) 0%, var(--grass-light) 60%, #d8c24a 100%); }
  .mailing-side .tip-panel { left: 0; top: 176px; width: 204px; height: 215px;
    background: linear-gradient(180deg, var(--plum) 0%, var(--plum-dark) 100%);
    color: var(--on-dark); font-size: 17.5px; line-height: 28px; padding: 10px 12px; }
  .mailing-side .photo-doctor { left: 204px; top: 176px; width: 148px; height: 215px;
    background: linear-gradient(180deg, #ececec 0%, var(--portrait) 55%, #7c8368 100%); }
  .mailing-side .contact-band { left: 0; top: 391px; width: 352px; height: 76px;
    background: linear-gradient(180deg, var(--olive) 0%, var(--olive-dark) 100%);
    color: var(--on-dark); text-align: center; padding-top: 6px; }
  .mailing-side .contact-band .cta { font-size: 26px; line-height: 32px; }
  .mailing-side .contact-band .details { font-size: 18.5px; line-height: 26px; }
  .mailing-side .return-address { left: 361px; top: 14px; color: var(--ink); }
  .brand-name { display: flex; align-items: center; gap: 8px; color: var(--plum); font-weight: 400; }
  .brand-name .mark { width: 12px; height: 12px; background: var(--olive); }
  .mailing-side .brand-name { font-size: 22px; }
  .mailing-side .address { margin-top: 20px; font-size: 13.5px; line-height: 17px; font-weight: 400; }

  /* offer side */
  .offer-side { left: 64px; top: 614px; width: 730px; height: 562px; }
  .offer-side .photo-flag-football { left: 0; top: 0; width: 365px; height: 256px;
    background: linear-gradient(180deg, #3d5a2a 0%, #5b7d35 45%, var(--grass) 75%, #86ac4a 100%); }
  .offer-side .message { left: 365px; top: 0; width: 365px; height: 256px;
    display: flex; align-items: center; justify-content: center; text-align: center;
    color: var(--ink); font-size: 23.5px; line-height: 35px; padding: 0 30px; }
  .offer-side .offer-panel { left: 0; top: 256px; width: 365px; height: 161px;
    background: linear-gradient(180deg, var(--plum) 0%, var(--plum-dark) 100%);
    color: var(--on-dark); text-align: center; padding-top: 16px; }
  .offer-side .offer-panel .free { font-size: 58px; line-height: 62px; }
  .offer-side .offer-panel .item { font-size: 40px; line-height: 50px; }
  .offer-side .photo-lacrosse { left: 365px; top: 256px; width: 365px; height: 161px;
    background: linear-gradient(135deg, #8fae6a 0%, var(--grass) 50%, #5a2a35 100%); }
  .offer-side .brand-panel { left: 0; top: 417px; width: 365px; height: 145px;
    background: linear-gradient(180deg, #ffffff 0%, #dcdcdc 100%);
    display: flex; align-items: center; justify-content: center; }
  .offer-side .brand-name { font-size: 34px; }
  .offer-side .brand-name .mark { width: 18px; height: 18px; }
  .offer-side .contact-panel { left: 365px; top: 417px; width: 365px; height: 145px;
    background: linear-gradient(180deg, var(--olive) 0%, var(--olive-dark) 100%);
    color: var(--on-dark); text-align: center; padding-top: 18px; }
  .offer-side .contact-panel .cta { font-size: 23px; line-height: 30px; }
  .offer-side .contact-panel .phone { font-size: 38px; line-height: 44px; font-weight: 400; }
  .offer-side .contact-panel .web { font-size: 22px; line-height: 28px; }
</style>
</head>
<body>
<main class="stage">

  <section class="postcard mailing-side">
    <div class="photo photo-player" role="img" aria-label="Young boy in a yellow jersey on a grass field"></div>
    <p class="block tip-panel">There are several types of mouthguards to choose from, and your doctor can help you choose the best one for your child's particular needs.</p>
    <div class="photo photo-doctor" role="img" aria-label="Portrait of the dentist"></div>
    <div class="block contact-band">
      <p class="cta">Contact Us Today!</p>
      <p class="details">(509) 738-1946 | CedarbrookDentist.example</p>
    </div>
    <div class="block return-address">
      <p class="brand-name"><span>Cedar Brook Dental</span><span class="mark"></span></p>
      <p class="address">22856 W. Larkfield Ave.<br>Suite B Mead, WA 99021</p>
    </div>
  </section>

  <section class="postcard offer-side">
    <div class="photo photo-flag-football" role="img" aria-label="Children playing flag football on a grass field"></div>
    <p class="block message">One of the best ways to prevent injury to your child's teeth and mouth while playing sports is to wear a mouthguard.</p>
    <div class="block offer-panel">
      <p class="free">Free</p>
      <p class="item">Sports Guards</p>
    </div>
    <div class="photo photo-lacrosse" role="img" aria-label="Girl playing lacrosse in a maroon jersey"></div>
    <div class="block brand-panel">
      <p class="brand-name"><span>Cedar Brook Dental</span><span class="mark"></span></p>
    </div>
    <div class="block contact-panel">
      <p class="cta">Contact Us Today!</p>
      <p class="phone">(509) 738-1946</p>
      <p class="web">CedarbrookDentist.example</p>
    </div>
  </section>

</main>
</body>
</html>
```